812 EDDM FLYER FOR CARPET CLEANING & WINDOW WASHING

Full Size Double Sided full color EDDM mailer

****PLEASE MAKE FONT TYPE, SIZE, COLOR, SPACING SAME AS IS EXAMPLE FLYER*******

***I have uploaded LOGO... It is on the VAN WRAP 812 CLEANING & RESTORATION

I have included an EDDM flyer and want my flyer to look like the example I uploaded.

I wanted to make it look Better & add my images and content. I have included the content under Must Haves......

Raindrop background

****Not all images will be used. Each service requires 2 images as seen on examply flyer... Please pic best 2 for each service, I can purchase new stock photo if needed

Target Market(s)

Residential Home Owners

Industry/Entity Type

Cleaning Service

Font styles to use
Serif

Colors
0555a3
ec1f27
fbed22
ffc214

Requirements
Must have
• Look Like Example EDDM postcard uploaded
• My images & content
• CARPET CLEANING Safe Eco-Friendly Truck Mounted Steam Cleaning. Say goodbye to those ugly carpet stains.
• WINDOW WASHING Interior/Exterior & Screens. Crystal Clear & Streak Free Windows
• POWER WASHING: Soft Wash & Power Wash. Safely cleans
• WATER DAMAGE: Got Mold or Water damage? Free IR Imaging Detection
• TILE & GROUT: Clean, Restore & Rejuvenate Tile, Grout & Stone
• MAINTENANCE: Professional & dependable repairs. We can Fit It!
• Call Today! 858-555-0147
• www.TidyNorth812.example
• ECO FRIENDLY CLEANING
• San Diego’s Trusted Cleaning Specialists

```html
<!DOCTYPE html>
<html lang="en">
<head>
<meta charset="utf-8">
<title>812 Cleaning &amp; Restoration – EDDM Mailer</title>
<link rel="stylesheet" href="https://fonts.googleapis.com/css2?family=Montserrat:wght@800&family=Roboto+Condensed:ital,wght@0,400;0,700;1,400;1,700;1,900&display=swap">
<style>
:root{
  --royal:#1d45d6;
  --royal-deep:#0f2fae;
  --navy:#13307f;
  --band-top:#aabcec;
  --band-bottom:#2a4cc4;
  --label-blue:#1a3fd0;
  --white:#ffffff;
  --ink:#222;
  --gold:#ffc214;
}
*{box-sizing:border-box;margin:0;padding:0}
html,body{width:1200px;height:1200px;overflow:hidden;background:var(--white)}
body{position:relative;font-family:"Roboto Condensed",sans-serif}

.card{
  position:absolute;left:251px;width:699px;height:526px;overflow:hidden;
  background:radial-gradient(ellipse at 30% 20%,#3a63ee 0%,var(--royal) 45%,var(--royal-deep) 100%);
  box-shadow:0 4px 14px rgba(0,0,0,.35);
}
.card--front{top:60px}
.card--back{top:614px}
.abs{position:absolute}

.offer-pill{
  background:var(--navy);border:2px solid var(--white);border-radius:10px;
  color:var(--white);font-style:italic;font-weight:400;font-size:29px;
  display:flex;align-items:center;justify-content:center;transform:scaleX(.92);
}
.band{
  border-radius:8px;
  background:linear-gradient(180deg,var(--band-top) 0%,#6f8ad9 45%,var(--band-bottom) 100%);
  display:flex;justify-content:center;
}
.band-title{
  font-family:"Montserrat",sans-serif;font-weight:800;color:var(--white);
  white-space:nowrap;letter-spacing:.5px;
}
.tag-pill{
  background:var(--white);border:2px solid var(--navy);border-radius:12px;
  color:var(--navy);font-style:italic;font-weight:900;text-align:center;
  display:flex;align-items:center;justify-content:center;line-height:1.25;
}

.photo{position:absolute;overflow:hidden}
.photo-label{
  position:absolute;left:0;right:0;bottom:14px;text-align:center;
  font-style:italic;font-weight:900;font-size:17px;color:var(--label-blue);
  text-shadow:-1px -1px 0 #fff,1px -1px 0 #fff,-1px 1px 0 #fff,1px 1px 0 #fff,0 0 3px #fff;
}
.ph-carpet{background:linear-gradient(160deg,#d8d8d4,#9d9d98)}
.ph-window{background:linear-gradient(180deg,#8a6a48 0%,#3c4c62 40%,#7d93ab 100%)}
.ph-power{background:linear-gradient(150deg,#2d3350 0%,#a5564a 35%,#b46a5c 100%)}
.ph-roof{background:linear-gradient(160deg,#a9c6e6 0%,#c4582c 35%,#9b4422 100%)}
.ph-tile{background:linear-gradient(160deg,#9a9a96,#6a6b68)}
.ph-maint{background:linear-gradient(150deg,#dfe6ee 0%,#c99a62 50%,#a87a48 100%)}

.info{
  position:absolute;background:var(--white);text-align:center;
  padding:10px 6px 0;color:var(--ink);font-size:8.5px;line-height:1.15;
}
.info-title{font-style:italic;font-weight:900;color:var(--label-blue);font-size:9.5px;margin-bottom:7px}
.info-hi{color:var(--label-blue);font-weight:700}

.brand{display:flex;align-items:center;gap:8px}
.brand-dot{width:50px;height:50px;border-radius:50%;background:var(--gold);flex:none}
.brand-name{color:var(--white);font-weight:700;font-size:21px;line-height:1.05}

.call{
  color:var(--white);font-style:italic;font-weight:400;font-size:20px;
  transform:rotate(-32deg);transform-origin:left bottom;white-space:nowrap;
}
.phone{
  color:var(--white);font-style:italic;font-weight:900;font-size:40px;
  letter-spacing:7px;white-space:nowrap;text-align:right;line-height:1;
}
.web{
  color:var(--white);font-style:italic;font-weight:900;font-size:36px;
  white-space:nowrap;text-align:right;line-height:1;letter-spacing:-.5px;
}

.mailbox{background:var(--white);color:#111}
.postage{
  border:1.5px solid #333;font-size:7.5px;line-height:1.15;text-align:center;
  padding:4px 2px;color:#333;
}
.postage b{font-size:9px;color:#111}
.ecrwss{font-size:11px;font-weight:700;letter-spacing:.3px}
.addressee{font-size:12px;font-weight:700;line-height:1.3}
</style>
</head>
<body>

<!-- FRONT -->
<section class="card card--front">
  <div class="abs band" style="left:7px;top:28px;width:684px;height:98px;align-items:center;padding-top:14px">
    <span class="band-title" style="font-size:39px">ECO FRIENDLY CLEANING</span>
  </div>
  <div class="abs offer-pill" style="left:210px;top:8px;width:278px;height:46px">We are offering</div>
  <div class="abs tag-pill" style="left:227px;top:118px;width:244px;height:55px;font-size:18px">San Diego’s Trusted<br>Cleaning Specialists</div>

  <div class="photo ph-carpet" style="left:7px;top:189px;width:224px;height:118px;border-top-left-radius:10px" role="img" aria-label="Freshly steam-cleaned carpet with cleaning lines">
    <span class="photo-label">CARPET CLEANING</span></div>
  <div class="photo ph-window" style="left:234px;top:189px;width:231px;height:118px" role="img" aria-label="Worker on ladder washing large glass windows">
    <span class="photo-label">WINDOW WASHING</span></div>
  <div class="photo ph-power" style="left:467px;top:189px;width:224px;height:118px;border-top-right-radius:10px" role="img" aria-label="Pressure washer cleaning red paving stones">
    <span class="photo-label">POWER WASHING</span></div>
  <div class="photo ph-roof" style="left:7px;top:311px;width:224px;height:115px;border-bottom-left-radius:10px" role="img" aria-label="Worker on a tiled roof near a skylight">
    <span class="photo-label">WATER DAMAGE</span></div>
  <div class="photo ph-tile" style="left:234px;top:311px;width:231px;height:115px" role="img" aria-label="Tile and grout cleaning machine on stone floor">
    <span class="photo-label">TILE &amp; GROUT</span></div>
  <div class="photo ph-maint" style="left:467px;top:311px;width:224px;height:115px;border-bottom-right-radius:10px" role="img" aria-label="Tool belt and hard hat at a framed construction site">
    <span class="photo-label">MAINTENANCE</span></div>

  <div class="abs brand" style="left:12px;top:440px;width:260px">
    <span class="brand-dot"></span>
    <span class="brand-name">812 CLEANING &amp;<br>RESTORATION</span>
  </div>
  <div class="abs call" style="left:290px;top:448px">Call Today!</div>
  <div class="abs phone" style="right:10px;top:437px">858-555-0147</div>
  <div class="abs web" style="right:12px;top:476px">www.TidyNorth812.example</div>
</section>

<!-- BACK -->
<section class="card card--back">
  <div class="abs band" style="left:7px;top:62px;width:407px;height:80px;justify-content:flex-start;padding:20px 0 0 20px">
    <span class="band-title" style="font-size:24.5px">ECO FRIENDLY CLEANING</span>
  </div>
  <div class="abs offer-pill" style="left:70px;top:17px;width:256px;height:43px">We are offering</div>
  <div class="abs tag-pill" style="left:28px;top:124px;width:359px;height:37px;font-size:17.5px">San Diego’s Trusted Cleaning Specialists</div>

  <div class="abs mailbox" style="left:442px;top:8px;width:249px;height:137px">
    <div class="abs postage" style="left:169px;top:7px;width:66px;height:57px">PRST STD<br>ECRWSS<br>U.S. POSTAGE<br><b>PAID</b><br>EDDM Retail</div>
    <div class="abs ecrwss" style="left:0;right:0;top:80px;text-align:center">********ECRWSS********</div>
    <div class="abs addressee" style="left:40px;top:100px">Local<br>Postal Customer</div>
  </div>

  <div class="photo ph-carpet" style="left:7px;top:190px;width:134px;height:116px;border-top-left-radius:10px" role="img" aria-label="Clean carpeted room with windows"></div>
  <div class="info" style="left:141px;top:190px;width:93px;height:116px">
    <div class="info-title">CARPET CLEANING</div>
    Safe Eco-Friendly Truck Mounted Steam Cleaning.<br><span class="info-hi">Say goodbye to those Ugly Carpet Stains.</span>
  </div>
  <div class="photo ph-window" style="left:234px;top:190px;width:134px;height:116px" role="img" aria-label="Worker on ladder washing tall windows"></div>
  <div class="info" style="left:368px;top:190px;width:99px;height:116px">
    <div class="info-title">WINDOW WASHING</div>
    Interior/Exterior, Screens, tracks, frames &amp; sills..<br><span class="info-hi">Crystal Clear &amp; Streak Free Windows</span>
  </div>
  <div class="photo ph-power" style="left:467px;top:190px;width:132px;height:116px" role="img" aria-label="Pressure washing red pavers"></div>
  <div class="info" style="left:599px;top:190px;width:92px;height:116px;border-top-right-radius:10px">
    <div class="info-title">POWER WASHING</div>
    House washing safe for siding, drives, patios &amp; walks .<br><span class="info-hi">It’s like an Instant Home Makeover</span>
  </div>

  <div class="info" style="left:7px;top:310px;width:106px;height:116px;padding-top:24px;border-bottom-left-radius:10px">
    <div class="info-title">WATER DAMAGE</div>
    Got Mold or Water damage?<br><span class="info-hi">Free IR Imaging &amp; Leak Detection</span>
  </div>
  <div class="photo ph-roof" style="left:113px;top:310px;width:118px;height:116px" role="img" aria-label="Worker inspecting a tiled roof"></div>
  <div class="info" style="left:231px;top:310px;width:119px;height:116px;padding-top:18px">
    <div class="info-title">TILE &amp; GROUT</div>
    Clean, Restore &amp; Rejuvenate Tile, Grout &amp; Stone<br><span class="info-hi">Renew Natural Luster</span>
  </div>
  <div class="photo ph-tile" style="left:350px;top:310px;width:115px;height:116px" role="img" aria-label="Tile cleaning machine on stone floor"></div>
  <div class="info" style="left:465px;top:310px;width:120px;height:116px;padding-top:22px">
    <div class="info-title">MAINTENANCE</div>
    Paint, Patch, Repair, Replace<br><span class="info-hi">YES! We can Fix It!</span>
  </div>
  <div class="photo ph-maint" style="left:585px;top:310px;width:106px;height:116px;border-bottom-right-radius:10px" role="img" aria-label="Tool belt and hard hat at a framed construction site"></div>

  <div class="abs brand" style="left:12px;top:440px;width:260px">
    <span class="brand-dot"></span>
    <span class="brand-name">812 CLEANING &amp;<br>RESTORATION</span>
  </div>
  <div class="abs call" style="left:290px;top:450px">Call Today!</div>
  <div class="abs phone" style="right:10px;top:439px">858-555-0147</div>
  <div class="abs web" style="right:12px;top:478px">www.TidyNorth812.example</div>
</section>

</body>
</html>
```